I am looking for a modern, clean and neat design for a reflexology and well being business. The business name is Lumen Orto (this is an old Latin word for wellbeing). The colours I would like are purple, white and grey. I am open to suggestions for pictures such as healing or working hands, a pair of feet, images that represent my business that you may think of....... or maybe you think no images at all would be best? My tag line is: "Relax, Renew, Revive" or "Find you balance......... Relax, Renew, Revive" I can decide which I want so I would like to see what both would look like. I would like space on the back to write the client's appointment date and time (more than once)

```html
<!DOCTYPE html>
<html lang="en">
<head>
<meta charset="utf-8">
<title>Lumen Orto – Business Card</title>
<link href="https://fonts.googleapis.com/css2?family=Comfortaa:wght@300;700&family=Montserrat:wght@400;700;800&family=Roboto:wght@400&display=swap" rel="stylesheet">
<style>
  :root {
    --bg: #e3e3e3;
    --card: #f4f4f5;
    --purple: #5e3a8c;
    --purple-light: #8a68b8;
    --panel: #7c55ad;
    --panel-text: #ffffff;
    --ink: #2a2a2e;
    --muted: #8a8a8f;
    --text: #3a3a3e;
  }
  * { box-sizing: border-box; margin: 0; padding: 0; }
  html, body {
    width: 1200px; height: 900px; overflow: hidden;
    background: var(--bg);
  }
  .canvas { position: relative; width: 1200px; height: 900px; }
  .card {
    position: absolute; left: 280px;
    width: 640px; height: 366px;
    background: var(--card);
    box-shadow: 0 2px 6px rgba(0,0,0,0.12);
    overflow: hidden;
  }
  .card-front { top: 58px; }
  .card-back { top: 476px; }

  /* Front */
  .brand {
    position: absolute; inset: 0;
    display: flex; flex-direction: column; align-items: center; justify-content: center;
  }
  .brand-row { display: flex; align-items: center; gap: 18px; }
  .brand-dot {
    width: 30px; height: 30px; border-radius: 50%;
    background: var(--purple-light);
  }
  .brand-name {
    font-family: "Comfortaa", sans-serif; font-weight: 700;
    font-size: 72px; color: var(--purple); letter-spacing: -1px; line-height: 1;
  }
  .tagline {
    margin-top: 14px;
    font-family: "Comfortaa", sans-serif; font-weight: 300;
    font-size: 40px; color: var(--purple); line-height: 1;
  }

  /* Back */
  .contact-side {
    position: absolute; left: 0; top: 0; width: 352px; height: 100%;
    padding: 62px 0 0 44px;
  }
  .person { display: flex; align-items: center; gap: 14px; }
  .person svg { width: 34px; height: 34px; }
  .person-name {
    font-family: "Montserrat", sans-serif; font-weight: 800;
    font-size: 24px; color: var(--ink); letter-spacing: -0.5px; line-height: 1;
  }
  .person-role {
    font-family: "Montserrat", sans-serif; font-weight: 400;
    font-size: 13px; color: var(--muted); letter-spacing: 0.5px; margin-top: 2px;
  }
  .contact-list { list-style: none; margin-top: 66px; }
  .contact-item {
    display: flex; align-items: center; gap: 16px; height: 40px;
    font-family: "Roboto", sans-serif; font-size: 18px; color: var(--text);
  }
  .contact-item svg { width: 30px; height: 30px; flex: none; }
  .appointment-side {
    position: absolute; right: 0; top: 0; width: 288px; height: 100%;
    background: var(--panel);
    padding: 56px 0 0 24px;
  }
  .appointment-title {
    font-family: "Montserrat", sans-serif; font-weight: 700;
    font-size: 19px; color: var(--panel-text); white-space: nowrap;
  }
</style>
</head>
<body>
<main class="canvas">

  <section class="card card-front">
    <div class="brand">
      <div class="brand-row">
        <span class="brand-dot"></span>
        <span class="brand-name">Lumen Orto</span>
      </div>
      <p class="tagline">Relax, Renew, Revive</p>
    </div>
  </section>

  <section class="card card-back">
    <div class="contact-side">
      <div class="person">
        <svg viewBox="0 0 34 34" fill="none" stroke="var(--purple-light)" stroke-width="1.8">
          <circle cx="17" cy="17" r="15"/>
          <circle cx="17" cy="13.5" r="5"/>
          <path d="M7.5 27c2.5-4.5 6-6.5 9.5-6.5s7 2 9.5 6.5"/>
        </svg>
        <div>
          <p class="person-name">JANE DOE</p>
          <p class="person-role">OWNER</p>
        </div>
      </div>
      <ul class="contact-list">
        <li class="contact-item">
          <svg viewBox="0 0 30 30" fill="none" stroke="var(--purple-light)" stroke-width="1.8">
            <rect x="8" y="3" width="14" height="24" rx="2"/>
            <line x1="8" y1="22" x2="22" y2="22"/>
          </svg>
          <span>123 456 789</span>
        </li>
        <li class="contact-item">
          <svg viewBox="0 0 30 30" fill="none" stroke="var(--purple-light)" stroke-width="1.8">
            <rect x="3" y="7" width="24" height="16"/>
            <path d="M3 7l12 10 12-10"/>
            <path d="M3 23l9-8M27 23l-9-8"/>
          </svg>
          <span>info@websiteurl.com</span>
        </li>
        <li class="contact-item">
          <svg viewBox="0 0 30 30" fill="none" stroke="var(--purple-light)" stroke-width="1.8">
            <circle cx="15" cy="15" r="12"/>
            <ellipse cx="15" cy="15" rx="5" ry="12"/>
            <line x1="3" y1="15" x2="27" y2="15"/>
            <path d="M5 9h20M5 21h20"/>
          </svg>
          <span>www.websiteurl.com</span>
        </li>
      </ul>
    </div>
    <div class="appointment-side">
      <p class="appointment-title">Your next appointment:</p>
    </div>
  </section>

</main>
</body>
</html>
```